Book Cover "Venice"

Creation of a cover (14 x 20.5 cm + bleed area) for a book:
Image: “BrumeVerte” (Tiff joined)
AUTHOR: Corinne Valmer
TITLE: The murmurs of Lorient
PUBLISHER: Editions Pluvane (AT THE BOTTOM OF THE COVER)

Target Market(s)

Readers of romantic novels

Industry/Entity Type

Book

```html
<!DOCTYPE html>
<html lang="fr">
<head>
<meta charset="utf-8">
<title>Les murmures de Lorient — Corinne Valmer</title>
<link rel="stylesheet" href="https://fonts.googleapis.com/css2?family=Great+Vibes&family=Playfair+Display:wght@400;700&display=swap">
<style>
  :root {
    --stage: #1c1c1c;
    --sky-top: #4e1420;
    --sky-mid: #a61e2a;
    --sky-glow: #d2381f;
    --sky-low: #7a1a1c;
    --skyline: #1a0a10;
    --gold: #c9a45c;
    --gold-light: #f3e2b8;
    --ivory: #fbf6ea;
  }
  html, body {
    margin: 0;
    width: 1200px;
    height: 1200px;
    overflow: hidden;
    background: var(--stage);
  }
  .cover {
    position: absolute;
    left: 206px;
    top: 26px;
    width: 788px;
    height: 1148px;
    overflow: hidden;
  }
  .cover-photo {
    position: absolute;
    inset: 0;
    background:
      radial-gradient(ellipse 70% 30% at 50% 66%, rgba(235, 80, 30, 0.55), transparent 70%),
      linear-gradient(180deg,
        var(--sky-top) 0%,
        var(--sky-mid) 22%,
        #8e1c2a 40%,
        var(--sky-glow) 62%,
        var(--sky-low) 74%,
        var(--skyline) 86%,
        var(--skyline) 100%);
  }
  .author {
    position: absolute;
    top: 70px;
    left: 0;
    right: 0;
    margin: 0;
    text-align: center;
    font-family: "Playfair Display", serif;
    font-weight: 700;
    font-size: 44px;
    letter-spacing: 1px;
    color: var(--gold);
  }
  .title {
    position: absolute;
    inset: 0;
    margin: 0;
    font-family: "Great Vibes", cursive;
    font-weight: 400;
  }
  .title span {
    position: absolute;
    white-space: nowrap;
    line-height: 1;
  }
  .title-les {
    left: 78px;
    top: 170px;
    font-size: 150px;
    color: var(--ivory);
  }
  .title-main {
    left: 70px;
    top: 330px;
    font-size: 176px;
    color: var(--gold-light);
  }
  .title-de {
    left: 520px;
    top: 478px;
    font-size: 70px;
    color: var(--gold);
  }
  .title-place {
    left: 190px;
    top: 500px;
    font-size: 170px;
    color: var(--ivory);
  }
  .publisher {
    position: absolute;
    bottom: 50px;
    left: 0;
    right: 0;
    margin: 0;
    text-align: center;
    font-family: "Playfair Display", serif;
    font-weight: 400;
    font-size: 36px;
    color: var(--ivory);
  }
</style>
</head>
<body>
  <main class="cover">
    <div class="cover-photo" role="img" aria-label="Photograph of a red sunset sky over a city skyline with a domed church silhouette and glowing street lamps"></div>
    <p class="author">Corinne Valmer</p>
    <h1 class="title">
      <span class="title-les">Les</span>
      <span class="title-main">murmures</span>
      <span class="title-de">de</span>
      <span class="title-place">Lorient</span>
    </h1>
    <p class="publisher">Editions Pluvane</p>
  </main>
</body>
</html>
```